New banner for sub page services (IT CLOUD INSPIRED)

We want a new website subpage banner / for our services page.
https://www.kortmeridian.nl/diensten/

We are a young IT (Cloud) company so the new banner has to contain:
- Our current logo
(https://www.kortmeridian.nl/wp-content/uploads/2021/03/logo.png)

- Our motto: ANALYZE VALIDATE ADVISE

- Some (IT) clouds examples (see examples for inspiration):
https://pixvarohost.io/g/QWTRMXkLpa

Banner size:
1280 bij 206 pixels

RAW LOGO SOURCE MATERIALS:
https://sendplumbox.io/data-package/7KmR42c9#link

```html
<!DOCTYPE html>
<html lang="nl">
<head>
<meta charset="utf-8">
<title>Kortmeridian – Diensten banner</title>
<link rel="stylesheet" href="https://fonts.googleapis.com/css2?family=Open+Sans:wght@400;700&display=swap">
<style>
  :root {
    --navy-deep: #06123d;
    --navy-mid: #0a2166;
    --navy-glow: #1a4fb0;
    --cyan-glow: #58c8ff;
    --panel-white: #ffffff;
    --wedge-grey: #6f6f6f;
    --brand-slate: #3f4b5d;
    --text-white: #ffffff;
  }
  * { margin: 0; padding: 0; box-sizing: border-box; }
  html, body {
    width: 1200px;
    height: 193px;
    overflow: hidden;
    background: var(--panel-white);
  }
  .banner {
    position: relative;
    width: 1200px;
    height: 193px;
    overflow: hidden;
    font-family: "Open Sans", Arial, sans-serif;
  }
  .banner__shapes {
    position: absolute;
    inset: 0;
  }
  .brand {
    position: absolute;
    left: 22px;
    top: 86px;
    width: 270px;
    text-align: center;
  }
  .brand__name {
    font-weight: 400;
    font-size: 40px;
    line-height: 1;
    color: var(--brand-slate);
    letter-spacing: -0.5px;
  }
  .motto {
    position: absolute;
    left: 392px;
    top: 75px;
    height: 45px;
    display: flex;
    align-items: center;
    gap: 22px;
    color: var(--text-white);
    font-weight: 700;
    font-size: 34.5px;
    line-height: 1;
    letter-spacing: 0.4px;
  }
  .motto__divider {
    display: block;
    width: 3px;
    height: 45px;
    background: var(--text-white);
  }
  .cloud-icon {
    position: absolute;
    left: 966px;
    top: 44px;
    width: 182px;
    height: 118px;
  }
</style>
</head>
<body>
  <div class="banner">
    <svg class="banner__shapes" width="1200" height="193" viewBox="0 0 1200 193">
      <defs>
        <radialGradient id="network-glow" cx="0.72" cy="0.3" r="0.75">
          <stop offset="0" stop-color="#1a4fb0"/>
          <stop offset="0.45" stop-color="#0a2166"/>
          <stop offset="1" stop-color="#06123d"/>
        </radialGradient>
      </defs>
      <polygon class="backdrop" points="361,0 1200,0 1200,193 380,193"
               fill="url(#network-glow)" role="img"
               aria-label="Dark blue digital backdrop with glowing network lines and a faint globe"/>
      <polygon class="wedge" points="342,66 305,193 380,193" fill="#6f6f6f"/>
    </svg>

    <div class="brand">
      <div class="brand__name">Kortmeridian</div>
    </div>

    <div class="motto">
      <span class="motto__word">ANALYZE</span>
      <span class="motto__divider"></span>
      <span class="motto__word">VALIDATE</span>
      <span class="motto__divider"></span>
      <span class="motto__word">ADVISE</span>
    </div>

    <svg class="cloud-icon" viewBox="0 0 180 118" aria-label="Cloud upload icon" role="img">
      <defs>
        <linearGradient id="arrow-fill" x1="0" y1="0" x2="0" y2="1">
          <stop offset="0" stop-color="#9fe3ff"/>
          <stop offset="1" stop-color="#2a7fe0"/>
        </linearGradient>
      </defs>
      <path d="M40 86 C18 86 8 72 10 60 C12 46 26 38 40 42 C42 22 62 8 84 10 C104 12 116 26 118 40 C126 34 142 34 150 44 C170 46 176 62 170 74 C166 82 158 86 148 86 Z"
            fill="rgba(40,110,220,0.25)" stroke="#58c8ff" stroke-width="2.5"/>
      <polygon points="90,50 72,70 83,70 83,112 97,112 97,70 108,70" fill="url(#arrow-fill)"/>
    </svg>
  </div>
</body>
</html>
```